Meadowlyn Acres Website Design

We have been redeveloping our website already and are quite happy with the content, but the design needs to be better:
https://harvo-link.example-host.com/

Pages, content, concept etc. Can all be taken from the redeveloped website.
The farmer can register and edit/view their profile, subscribe and these pages need to be designed better as well as contact, about, pricing, tos, privacy and a page with example portlets.

We need a website to appeal to farmers, investors and retiring farmers.

The design should be clean and a little country.

We don't want any repeat designs that some may submit to every project and has no respect for the project brief, so please don't submit them.

Target Market(s)

farmers, investors, retirees

Industry/Entity Type

Farming

Number of Pages Required

5+ page

Colors

Designer to choose colors to be used in the design.

Requirements
Must have
• Nice, clean modern design that is appealing
• Profile page laid out nicely

```html
<!DOCTYPE html>
<html lang="en">
<head>
<meta charset="utf-8">
<title>Meadowlyn Acres</title>
<link href="https://fonts.googleapis.com/css2?family=Lato:ital,wght@0,400;0,700;0,900;1,400;1,700&display=swap" rel="stylesheet">
<style>
:root{
  --green:#22a235;
  --green-dark:#0f6b1d;
  --green-deep:#0c5a18;
  --green-light:#3dd25a;
  --white:#ffffff;
  --ink:#555555;
  --muted:#9a9a9a;
  --footer:#232323;
  --footer-line:#3b3b3b;
  --footer-text:#b9b9b9;
}
*{margin:0;padding:0;box-sizing:border-box}
html,body{width:979px;height:1200px;overflow:hidden;background:var(--white)}
body{position:relative;font-family:'Lato',sans-serif;color:var(--ink)}
.abs{position:absolute}

/* hero */
.hero{left:0;top:0;width:979px;height:286px;background:radial-gradient(ellipse at 60% 40%,#3bc94a 0%,#1f9a2c 45%,#15751f 100%)}
.hero-title{left:0;top:30px;width:979px;text-align:center;color:var(--white);font-weight:900;font-size:29px;letter-spacing:-.3px}
.step{top:0;width:170px;margin-left:-85px;text-align:center}
.step-ring{position:absolute;left:50px;top:107px;width:68px;height:68px;border:2px solid var(--white);border-radius:50%}
.step-ring svg{position:absolute;left:16px;top:16px}
.step-num{position:absolute;left:34px;top:98px;width:32px;height:32px;border-radius:50%;background:var(--white);color:var(--green);font-weight:900;font-size:16px;line-height:32px;text-align:center}
.step-text{position:absolute;left:0;top:187px;width:170px;color:var(--white);font-weight:900;font-size:11.5px;line-height:11px;letter-spacing:-.3px}
.step-btn{position:absolute;left:47px;top:224px;width:76px;height:20px;background:var(--white);color:var(--green-dark);font-weight:700;font-size:8px;line-height:20px}

/* team */
.arrow{top:358px}
.avatar{top:347px;width:74px;height:74px;border-radius:50%;border:3px solid #d4d4d4;background:radial-gradient(circle at 50% 40%,#7d8a98,#4e5a68)}
.avatar.active{border-color:var(--green);background:radial-gradient(circle at 50% 40%,#c9b7a5,#6d5a4d)}
.member-name{left:0;top:438px;width:979px;text-align:center;color:var(--green);font-size:15px;font-weight:400}
.member-role{left:0;top:458px;width:979px;text-align:center;font-size:11px;color:#666}
.member-bio{left:255px;top:478px;width:470px;text-align:center;font-size:9px;line-height:12.5px;color:var(--muted)}

/* newsletter */
.newsletter{left:107px;top:552px;width:765px;height:76px;background:var(--green)}
.nl-title{left:134px;top:583px;color:var(--white);font-size:11.5px;font-weight:700}
.nl-sub{left:236px;top:584px;color:var(--white);font-size:8px;font-style:italic}
.nl-input{left:597px;top:575px;width:176px;height:30px;border:1px solid #9fe0a8;color:var(--white);font-size:8px;font-style:italic;line-height:28px;padding-left:36px}
.nl-input svg{position:absolute;left:13px;top:10px}
.nl-btn{left:786px;top:575px;width:60px;height:30px;background:var(--green-deep);color:var(--white);font-size:8.5px;line-height:30px;text-align:center}

/* audiences */
.panel-photo{left:0;top:681px;width:490px;height:256px;background:linear-gradient(160deg,#4c5a43 0%,#3a3b2e 40%,#2a2a22 75%,#5a5640 100%)}
.panel-green{left:490px;top:681px;width:489px;height:256px;background:radial-gradient(ellipse at 70% 30%,#3ccb4c 0%,#20982c 50%,#137a1e 100%)}
.panel-title{color:var(--white);font-size:18.5px;font-weight:700;letter-spacing:-.3px}
.panel-copy{color:var(--white);font-size:14.2px;line-height:14.7px;letter-spacing:-.2px}
.panel-btn{top:853px;width:133px;height:34px;color:var(--white);font-size:12.5px;text-align:center;line-height:34px;box-shadow:0 2px 3px rgba(0,0,0,.3)}
.btn-bright{background:var(--green)}
.btn-dark{background:var(--green-deep)}

/* footer */
.footer{left:0;top:986px;width:979px;height:171px;background:var(--footer)}
.f-head{top:1015px;color:var(--white);font-size:11.5px;font-weight:700}
.f-rule{top:1032px;width:162px;height:1px;background:var(--footer-line)}
.f-list{top:1036px;list-style:none}
.f-list li{width:138px;height:20.5px;border-bottom:1px solid var(--footer-line);font-size:7.5px;line-height:20px;color:var(--footer-text);padding-left:8px;position:relative}
.f-list li:last-child{border-bottom:none}
.f-list li::before{content:"";position:absolute;left:0;top:9px;width:3px;height:3px;background:var(--green)}
.f-label{color:var(--footer-text);font-size:8px;font-weight:700}
.f-value{color:#8d8d8d;font-size:7px;line-height:12px}
.social{left:678px;width:140px;height:20px}
.social .sq{position:absolute;left:0;top:3px;width:15px;height:15px;background:#1e88d6}
.social .t1{position:absolute;left:21px;top:0;color:var(--footer-text);font-size:8px;font-weight:700}
.social .t2{position:absolute;left:21px;top:10px;color:#8d8d8d;font-size:7px}
.legal{left:0;top:1157px;width:979px;height:43px;background:var(--green);color:var(--white);font-size:7px;text-align:center;line-height:14px;padding-top:8px}
</style>
</head>
<body>

<section class="abs hero" role="img" aria-label="Blurred green crop field background"></section>
<h1 class="abs hero-title">ASPIRING FARMERS</h1>

<div class="abs step" style="left:305px">
  <div class="step-ring"><svg width="32" height="32" viewBox="0 0 32 32" fill="#fff"><circle cx="10" cy="7" r="3.5"/><rect x="6" y="12" width="8" height="9"/><rect x="4" y="18" width="24" height="3"/><rect x="18" y="21" width="3" height="9"/><circle cx="23" cy="9" r="3"/><rect x="20" y="13" width="6" height="5"/></svg></div>
  <div class="step-num">1</div>
  <div class="step-text">REGISTER AS AN<br>ASPIRING FARMER</div>
  <div class="step-btn">REGISTER</div>
</div>
<div class="abs step" style="left:466px">
  <div class="step-ring"><svg width="32" height="32" viewBox="0 0 32 32" fill="#fff"><rect x="10" y="6" width="10" height="8"/><rect x="6" y="13" width="20" height="6"/><circle cx="10" cy="23" r="6"/><circle cx="10" cy="23" r="2.5" fill="#22a235"/><circle cx="24" cy="24" r="4"/><circle cx="24" cy="24" r="1.5" fill="#22a235"/></svg></div>
  <div class="step-num">2</div>
  <div class="step-text">BUILD YOUR FARM SKILLS TO<br>GET YOURSELF FARM-READY.</div>
  <div class="step-btn">FARM READY</div>
</div>
<div class="abs step" style="left:657px">
  <div class="step-ring"><svg width="32" height="32" viewBox="0 0 32 32" fill="#fff"><path d="M4 16 Q16 8 28 16 Q26 28 16 30 Q6 28 4 16Z"/><path d="M10 20 Q16 14 22 20" stroke="#22a235" stroke-width="2" fill="none"/><rect x="15" y="2" width="2" height="6"/><rect x="8" y="5" width="2" height="5" transform="rotate(-30 9 7)"/><rect x="22" y="5" width="2" height="5" transform="rotate(30 23 7)"/></svg></div>
  <div class="step-num">3</div>
  <div class="step-text">TOGETHER WE FIND YOU<br>YOUR DREAM FARM.</div>
  <div class="step-btn">MATCH MAKING</div>
</div>

<svg class="abs arrow" style="left:259px" width="26" height="54" viewBox="0 0 26 54"><path d="M24 1 L2 27 L24 53" fill="none" stroke="#777" stroke-width="2.5"/></svg>
<svg class="abs arrow" style="left:691px" width="26" height="54" viewBox="0 0 26 54"><path d="M2 1 L24 27 L2 53" fill="none" stroke="#777" stroke-width="2.5"/></svg>
<div class="abs avatar" style="left:303px" role="img" aria-label="Team member portrait"></div>
<div class="abs avatar active" style="left:401px" role="img" aria-label="Portrait of Tom Harlow"></div>
<div class="abs avatar" style="left:499px" role="img" aria-label="Team member portrait"></div>
<div class="abs avatar" style="left:597px" role="img" aria-label="Team member portrait"></div>
<div class="abs member-name">TOM HARLOW</div>
<div class="abs member-role">Designation: CEO</div>
<p class="abs member-bio">Lorem ipsum dolor sit amet, consectetur adipiscing elit. Donec dignissim risus risus, nec iaculis quam porttitor et. Ut mattis magna vitae massa luctus fermentum.</p>

<section class="abs newsletter"></section>
<div class="abs nl-title">NEWS LETTER</div>
<div class="abs nl-sub">join us now to get all news and special offers</div>
<div class="abs nl-input"><svg width="12" height="9" viewBox="0 0 12 9"><rect x=".5" y=".5" width="11" height="8" fill="none" stroke="#fff"/><path d="M.5 .5 L6 5 L11.5 .5" fill="none" stroke="#fff"/></svg>type your email here</div>
<div class="abs nl-btn">JOIN US</div>

<section class="abs panel-photo" role="img" aria-label="Photo of a farming family seated outdoors among trees and tall grass"></section>
<h2 class="abs panel-title" style="left:142px;top:720px">INVESTORS</h2>
<p class="abs panel-copy" style="left:142px;top:748px;width:330px">We have the best farmers in Australia ready to work with you on your farm.<br>Simply browse the list and decide who you want to work with. No registration required and your information will be kept private.</p>
<div class="abs panel-btn btn-bright" style="left:141px">SIGN UP NOW</div>
<div class="abs panel-btn btn-dark" style="left:288px">FIND OUT MORE</div>

<section class="abs panel-green" role="img" aria-label="Blurred green crop field background"></section>
<h2 class="abs panel-title" style="left:520px;top:720px">RETIRING FARMERS</h2>
<p class="abs panel-copy" style="left:522px;top:748px;width:310px">Are you looking for a positive way to step back from your farm?<br>We can connect you with a passionate aspiring farming family who will love your farm just as much as you do. No registration required and your information will be kept private</p>
<div class="abs panel-btn btn-dark" style="left:520px">INQUIRE NOW</div>
<div class="abs panel-btn btn-dark" style="left:666px">FIND OUT MORE</div>

<footer class="abs footer"></footer>
<h3 class="abs f-head" style="left:141px">PRODUCTS</h3>
<div class="abs f-rule" style="left:141px"></div>
<ul class="abs f-list" style="left:141px"><li>Home Emergency Cover</li><li>Multi Appliance Cover</li><li>Silver Cover</li><li>Gold Cover</li><li>Platinum Cover</li></ul>

<h3 class="abs f-head" style="left:320px">FIELDSTONE SUPPORT Ltd</h3>
<div class="abs f-rule" style="left:320px"></div>
<ul class="abs f-list" style="left:320px"><li>About Us</li><li>FAQ</li><li>Contact Us</li><li>Terms &amp; Conditions</li><li>Privacy Policy</li></ul>

<h3 class="abs f-head" style="left:499px">CONTACT INFO</h3>
<div class="abs f-rule" style="left:499px"></div>
<div class="abs f-label" style="left:499px;top:1041px">Phone Number</div>
<div class="abs f-value" style="left:499px;top:1055px">+44 900 118 274<br>+44 900 552 036</div>
<div class="abs" style="left:499px;top:1084px;width:84px;height:1px;background:var(--footer-line)"></div>
<div class="abs f-label" style="left:499px;top:1096px">Email Address</div>
<div class="abs f-value" style="left:499px;top:1110px">contact@meadowlyn.example<br>support@meadowlyn.example</div>

<h3 class="abs f-head" style="left:678px">FIND US ON SOCIAL</h3>
<div class="abs f-rule" style="left:678px"></div>
<div class="abs social" style="top:1045px"><span class="sq"></span><span class="t1">Find Us</span><span class="t2">on Friendspace</span></div>
<div class="abs social" style="top:1076px"><span class="sq"></span><span class="t1">Follow Us</span><span class="t2">on Workline</span></div>
<div class="abs social" style="top:1106px"><span class="sq"></span><span class="t1">Follow Us</span><span class="t2">on Chirper</span></div>

<div class="abs legal">Copyright 2015 &nbsp;|&nbsp; All Rights Reserved &nbsp;|&nbsp; Fieldstone Success.<br>Meadowlyn Acres is An Appointed Representative which is Authorised and Regulated by the Rural Standards Council</div>

</body>
</html>
```